Service business needs Business Card Design

Looking to create a new business card design that is both professional and unique the can highlight the many services we offer throughout the seasons. Our tagline is "The Steadfast Touch"
Licensed & Insured: PA392617 has to be small and on the back side of the card.
On the Front:
FirstName LastName
Title
We offer the following services:
Deck Repair and Maintenance
Deck Cleaning and Staining/Painting
Power Washing/House Washing
Landscape Lighting Installation
Christmas Lighting Installation

```html
<!DOCTYPE html>
<html lang="en">
<head>
<meta charset="utf-8">
<title>Clearview Services – Business Card</title>
<link rel="stylesheet" href="https://fonts.googleapis.com/css2?family=Michroma&family=Montserrat:wght@400;500;600;700&display=swap">
<style>
  :root {
    --bg: #cfcfcf;
    --sky-light: #4cc7f2;
    --sky-mid: #2a9fdc;
    --sky-deep: #1372b5;
    --navy: #0b4f8e;
    --brand-blue: #1a5fa6;
    --ink: #1d1d1f;
    --paper: #ffffff;
    --wash: #e4eef7;
  }
  * { box-sizing: border-box; margin: 0; padding: 0; }
  html, body { width: 1200px; height: 900px; overflow: hidden; }
  body {
    background: var(--bg);
    font-family: "Montserrat", sans-serif;
    position: relative;
  }
  .card {
    position: absolute;
    width: 620px;
    height: 354px;
    border-radius: 30px;
    overflow: hidden;
    box-shadow: 0 6px 18px rgba(0,0,0,0.25);
  }

  /* Services side */
  .card--services {
    left: 80px; top: 80px;
    background: linear-gradient(200deg, var(--sky-light) 0%, var(--sky-mid) 45%, var(--sky-deep) 100%);
    color: var(--paper);
  }
  .card--services .sheen {
    position: absolute; inset: 0;
    background: radial-gradient(ellipse at 90% 20%, rgba(255,255,255,0.22), rgba(255,255,255,0) 60%);
  }
  .services {
    position: absolute;
    left: 150px; top: 110px;
    font-family: "Michroma", sans-serif;
    text-transform: uppercase;
  }
  .services__heading {
    font-size: 14px; font-weight: 700; letter-spacing: 1px;
    margin-bottom: 16px;
  }
  .services__list { list-style: none; font-size: 12.5px; line-height: 1.45; }

  /* Contact side */
  .card--contact {
    left: 500px; top: 470px;
    background: var(--paper);
  }
  .card--contact .wash {
    position: absolute; right: 0; top: 0; width: 62%; height: 100%;
    background: linear-gradient(225deg, var(--wash) 0%, rgba(228,238,247,0) 75%);
  }
  .brand {
    position: absolute; left: 86px; top: 78px;
    font-family: "Michroma", sans-serif;
    color: var(--brand-blue);
    display: flex; align-items: center; gap: 10px;
  }
  .brand__dot { width: 14px; height: 14px; border-radius: 50%; background: var(--brand-blue); }
  .brand__name { font-size: 22px; letter-spacing: 1px; }
  .person { position: absolute; left: 100px; top: 140px; }
  .person__name {
    font-family: "Michroma", sans-serif; font-size: 19px; color: var(--navy);
    letter-spacing: 0.5px;
  }
  .person__title { font-size: 16px; color: var(--ink); margin-top: 2px; }
  .contacts { list-style: none; position: absolute; left: 100px; top: 210px; }
  .contacts li {
    display: flex; align-items: center; gap: 10px;
    font-size: 15px; color: var(--ink); line-height: 1.55;
  }
  .contacts svg { width: 16px; height: 16px; fill: var(--navy); }
  .license {
    position: absolute; right: 50px; bottom: 78px;
    font-size: 14px; color: var(--brand-blue);
  }
  .license__number { color: var(--ink); }
  .tagline-band {
    position: absolute; left: 0; right: 0; bottom: 0; height: 56px;
    background: var(--navy);
    display: flex; align-items: center; justify-content: flex-end;
    padding-right: 60px;
  }
  .tagline {
    font-family: "Michroma", sans-serif; color: var(--paper);
    font-size: 17px; letter-spacing: 2px; text-transform: uppercase;
  }
</style>
</head>
<body>

<section class="card card--services">
  <div class="sheen"></div>
  <div class="services">
    <h2 class="services__heading">We offer the following services</h2>
    <ul class="services__list">
      <li>Deck Repair and Maintenance</li>
      <li>Deck Cleaning and Staining/Painting</li>
      <li>Power Washing/House Washing</li>
      <li>Landscape Lighting Installation</li>
      <li>Christmas Lighting Installation</li>
    </ul>
  </div>
</section>

<section class="card card--contact">
  <div class="wash"></div>
  <div class="brand">
    <span class="brand__dot"></span>
    <span class="brand__name">CLEARVIEW SERVICES</span>
  </div>
  <div class="person">
    <p class="person__name">DANIEL HARPER</p>
    <p class="person__title">Managing Director</p>
  </div>
  <ul class="contacts">
    <li>
      <svg viewBox="0 0 24 24"><path d="M6.6 10.8a15 15 0 0 0 6.6 6.6l2.2-2.2a1 1 0 0 1 1-.25 11.4 11.4 0 0 0 3.6.6 1 1 0 0 1 1 1V20a1 1 0 0 1-1 1A17 17 0 0 1 3 4a1 1 0 0 1 1-1h3.5a1 1 0 0 1 1 1c0 1.25.2 2.45.6 3.6a1 1 0 0 1-.25 1z"/></svg>
      044-987 654 321
    </li>
    <li>
      <svg viewBox="0 0 24 24"><path d="M2 5h20v14H2zm2 2v.5l8 5 8-5V7l-8 5z"/></svg>
      info@clearviewsvc.com
    </li>
    <li>
      <svg viewBox="0 0 24 24"><path d="M12 2a10 10 0 1 0 0 20 10 10 0 0 0 0-20zm6.9 6h-3a15 15 0 0 0-1.3-3.9A8 8 0 0 1 18.9 8zM12 4c.8 1.2 1.5 2.5 1.9 4h-3.8c.4-1.5 1.1-2.8 1.9-4zM4.3 14a8 8 0 0 1 0-4h3.4a16 16 0 0 0 0 4zm.8 2h3a15 15 0 0 0 1.3 3.9A8 8 0 0 1 5.1 16zm3-8h-3a8 8 0 0 1 4.3-3.9A15 15 0 0 0 8.1 8zM12 20c-.8-1.2-1.5-2.5-1.9-4h3.8c-.4 1.5-1.1 2.8-1.9 4zm2.3-6H9.7a14 14 0 0 1 0-4h4.6a14 14 0 0 1 0 4zm.3 5.9a15 15 0 0 0 1.3-3.9h3a8 8 0 0 1-4.3 3.9zm1.7-5.9a16 16 0 0 0 0-4h3.4a8 8 0 0 1 0 4z"/></svg>
      www.clearviewsvc.com
    </li>
  </ul>
  <p class="license">Licensed &amp; Insured: <span class="license__number">PA392617</span></p>
  <div class="tagline-band">
    <p class="tagline">The Steadfast Touch</p>
  </div>
</section>

</body>
</html>
```